6"x9" Postcard Mailer

A 6"x9" Postcard mailer targeted to forensic laboratories to advertise or mock forensic samples (https://veltrasync.example/products/mock-forensic-samples/).

Here is some copy, but we can modify if there is not enough space:

Headline:
Expedite Training, Validation, & R&D with Our Ready-to-Use Mock Samples

Bullet Points:

- Wide Variety of Sample Types: IRB-approved samples mimicking crime scene substances, including semen, hair, bone, saliva, blood, and vaginal epithelial cells.
- Diverse Scenarios: Simulate sexual assault and degraded samples for varied conditions.
- Custom Solutions: Tailored DNA quantities and concentrations to suit your lab's needs.

Use discount code PRAX47 for a 10% discount

```html
<!DOCTYPE html>
<html lang="en">
<head>
<meta charset="utf-8">
<title>Veltrasync Mock Samples Postcard</title>
<link rel="stylesheet" href="https://fonts.googleapis.com/css2?family=Source+Sans+3:ital,wght@0,400;0,700;1,400&display=swap">
<style>
  :root {
    --backdrop: #d3d3d5;
    --paper: #ffffff;
    --brand-blue: #2555a3;
    --sky-blue: #2b8fd0;
    --ink: #1a1a1a;
    --night: #050507;
    --photo-deep: #0d1a3a;
    --photo-glove: #2f5fc4;
    --photo-bench: #d9d9dc;
  }
  * { margin: 0; padding: 0; box-sizing: border-box; }
  html, body { width: 1200px; height: 440px; overflow: hidden; background: var(--backdrop); }
  body { position: relative; font-family: "Source Sans 3", "Myriad Pro", sans-serif; color: var(--ink); }

  .postcard { position: absolute; top: 33px; width: 547px; height: 367px; background: var(--paper); overflow: hidden; }
  .postcard--front { left: 26px; }
  .postcard--back { left: 625px; }
  .postcard__art { position: absolute; inset: 0; width: 100%; height: 100%; }

  .brand-name { position: absolute; left: 12px; top: 33px; font-size: 18px; font-weight: 400; color: var(--brand-blue); letter-spacing: 0.2px; }

  .contact { position: absolute; left: 19px; top: 164px; list-style: none; color: var(--paper); font-size: 9.5px; }
  .contact__item { display: flex; align-items: center; gap: 6px; height: 13px; margin-bottom: 6px; }
  .contact__icon { width: 13px; height: 13px; flex: none; }

  .headline { position: absolute; left: 60px; width: 410px; top: 257px; text-align: center; color: var(--paper); font-size: 27px; line-height: 34px; font-weight: 400; }
  .headline__product { display: block; font-weight: 700; letter-spacing: 2px; }

  .benefits { position: absolute; left: 192px; top: 35px; width: 270px; list-style: none; font-size: 12.2px; line-height: 15px; }
  .benefits__item { position: absolute; left: 0; width: 270px; }
  .benefits__item:nth-child(1) { top: 0; }
  .benefits__item:nth-child(2) { top: 90px; width: 250px; }
  .benefits__item:nth-child(3) { top: 150px; width: 180px; }

  .offer { position: absolute; left: 20px; top: 294px; color: var(--paper); font-size: 19px; line-height: 24px; }
  .offer__code { font-style: italic; }
  .offer__value { font-size: 25px; font-weight: 700; }
  .offer__line--last { margin-top: 6px; }
</style>
</head>
<body>

<section class="postcard postcard--front">
  <svg class="postcard__art" viewBox="0 0 1173 788" preserveAspectRatio="none" aria-hidden="false">
    <defs>
      <linearGradient id="labPhotoTone" x1="0" y1="0" x2="1" y2="1">
        <stop offset="0" stop-color="var(--photo-deep)"/>
        <stop offset="0.45" stop-color="var(--photo-glove)"/>
        <stop offset="1" stop-color="var(--photo-bench)"/>
      </linearGradient>
    </defs>
    <polygon fill="url(#labPhotoTone)" points="302,0 1173,0 1173,580 360,500 330,160" role="img" aria-label="Photo: gloved hands swabbing a blood stain on a lab bench, holding a ring"/>
    <polygon fill="var(--sky-blue)" points="0,285 263,165 290,80 315,80 382,495 345,490 0,650"/>
    <polygon fill="var(--brand-blue)" points="0,650 345,490 1173,570 1173,788 0,788"/>
  </svg>

  <div class="brand-name">Veltrasync</div>

  <ul class="contact">
    <li class="contact__item">
      <svg class="contact__icon" viewBox="0 0 20 20"><circle cx="10" cy="10" r="10" fill="var(--brand-blue)"/><path d="M7 5.5l1.6 2.3-1 1.2a7 7 0 0 0 3.4 3.4l1.2-1 2.3 1.6-.9 1.6C9.5 14.5 5.5 10.5 5.4 6.4z" fill="#fff"/></svg>
      <span>+1 555 014 2290</span>
    </li>
    <li class="contact__item">
      <svg class="contact__icon" viewBox="0 0 20 20"><circle cx="10" cy="10" r="10" fill="var(--brand-blue)"/><rect x="5.5" y="7" width="9" height="6.5" fill="#fff"/><path d="M5.5 7l4.5 3.5L14.5 7" fill="none" stroke="var(--brand-blue)" stroke-width="1"/></svg>
      <span>info@veltrasync.example</span>
    </li>
  </ul>

  <h1 class="headline">Expedite Training, Validation, and R&amp;D with Our Ready-to-Use <span class="headline__product">MOCK SAMPLES</span></h1>
</section>

<section class="postcard postcard--back">
  <svg class="postcard__art" viewBox="0 0 1173 788" preserveAspectRatio="none">
    <defs>
      <radialGradient id="helixTone" cx="0.5" cy="0.5" r="0.5">
        <stop offset="0" stop-color="#dfe3f3"/>
        <stop offset="1" stop-color="#ffffff" stop-opacity="0"/>
      </radialGradient>
      <linearGradient id="kitPhotoTone" x1="0" y1="0" x2="1" y2="1">
        <stop offset="0" stop-color="#1b2233"/>
        <stop offset="0.5" stop-color="#d8e1ee"/>
        <stop offset="1" stop-color="#142038"/>
      </linearGradient>
    </defs>
    <ellipse cx="850" cy="380" rx="300" ry="290" fill="url(#helixTone)" role="img" aria-label="Faint DNA double helix decoration"/>
    <polygon fill="var(--night)" points="0,0 275,0 433,645 230,550 0,570"/>
    <rect x="20" y="110" width="285" height="190" rx="14" fill="url(#kitPhotoTone)" opacity="0.55" role="img" aria-label="Photo: two mock sample kit boxes, one open showing vials"/>
    <polygon fill="var(--brand-blue)" points="0,570 230,550 538,695 540,788 0,788"/>
  </svg>

  <ul class="benefits">
    <li class="benefits__item">Wide Variety of Sample Types: IRB-approved samples mimicking crime scene substances, including semen, hair, bone, saliva, blood, and vaginal epithelial cells.</li>
    <li class="benefits__item">Diverse Scenarios: Simulate sexual assault and degraded samples for varied conditions.</li>
    <li class="benefits__item">Custom Solutions: Tailored DNA quantities and concentrations to suit your lab's needs.</li>
  </ul>

  <p class="offer">
    <span class="offer__line">Use discount</span><br>
    <span class="offer__line">code <span class="offer__code">PRAX47</span></span><br>
    <span class="offer__line offer__line--last">for a <span class="offer__value">10% discount</span></span>
  </p>
</section>

</body>
</html>
```